Natural Please look at the foto, someting like this

We want 4 Cleaners: Bathcleaner ( content is Red ), Kichen degreeser ( the content is Yellow ), Glasscleaner Content is Blue) and all Purpus cleaner the content is green ) .
Unless you are saing that is has to be Transparant.
In a 750ml transparent Spray bottle
It are Natural products, with natural Parfume, Biodegradable
packeging is Recycled Plastic. Vegan, Bio, Eco Friendly , Green,
Natural Glu, Natural Ink.
these cries must come on the front.
The Logo is Doctor Quaffel, but we want That Green!!!!
People have to see immidiatly that the products are GREEN And Natural etc.
We want you to think about a nice name a slogen,
For excample: Powerd by Nature,
Use if you cant think of one.
And we want that to on the front.
For now you only have to make the fronts!!

```html
<!DOCTYPE html>
<html lang="en">
<head>
<meta charset="utf-8">
<title>Doctor Quaffel – All Purpus cleaner label</title>
<link href="https://fonts.googleapis.com/css2?family=Montserrat:wght@600;700;800&family=Yellowtail&display=swap" rel="stylesheet">
<style>
  :root {
    --page-bg: #f1f8f2;
    --label-green-light: #b3d83a;
    --label-green-mid: #49b83f;
    --label-green-deep: #0d8b45;
    --glow-lime: #c9ec3c;
    --name-yellow: #e6f53a;
    --slogan-ink: #0b0b0b;
    --band-dark: #0a1a0c;
    --band-edge: #1e4a1f;
    --band-text: #ffffff;
    --volume-yellow: #f3ef2c;
  }
  * { box-sizing: border-box; margin: 0; padding: 0; }
  html, body {
    width: 1200px;
    height: 997px;
    overflow: hidden;
    background: var(--page-bg);
  }
  .canvas {
    position: relative;
    width: 1200px;
    height: 997px;
  }
  .label {
    position: absolute;
    left: 250px;
    top: 48px;
    width: 700px;
    height: 900px;
    overflow: hidden;
    border-radius: 350px 350px 180px 180px / 350px 350px 180px 180px;
    background:
      linear-gradient(200deg, rgba(255,255,255,0.18) 0%, rgba(255,255,255,0) 35%),
      linear-gradient(110deg, var(--label-green-light) 0%, var(--label-green-mid) 45%, var(--label-green-deep) 100%);
  }
  .label__emblem-area {
    position: absolute;
    left: 16px;
    top: 46px;
    width: 668px;
    height: 668px;
    border-radius: 50%;
    background: radial-gradient(circle at 50% 50%,
      rgba(40,160,60,0.55) 0%,
      rgba(60,175,55,0.45) 40%,
      rgba(201,236,60,0.55) 58%,
      rgba(120,200,70,0.25) 75%,
      rgba(255,255,255,0) 100%);
  }
  .label__brand {
    position: absolute;
    left: 0;
    right: 0;
    top: 190px;
    text-align: center;
    font-family: "Montserrat", sans-serif;
    font-weight: 800;
    font-size: 104px;
    line-height: 1.05;
    letter-spacing: -2px;
    color: var(--name-yellow);
  }
  .label__slogan {
    position: absolute;
    left: 0;
    right: 0;
    top: 572px;
    text-align: center;
    font-family: "Yellowtail", cursive;
    font-size: 80px;
    line-height: 1;
    color: var(--slogan-ink);
  }
  .label__band {
    position: absolute;
    left: 0;
    right: 0;
    top: 712px;
    height: 75px;
    display: flex;
    align-items: center;
    justify-content: center;
    background: linear-gradient(90deg, var(--band-edge) 0%, var(--band-dark) 25%, var(--band-dark) 75%, #000 100%);
  }
  .label__product {
    font-family: "Montserrat", sans-serif;
    font-weight: 600;
    font-size: 48px;
    letter-spacing: 1px;
    color: var(--band-text);
  }
  .label__volume {
    position: absolute;
    left: 0;
    right: 0;
    top: 838px;
    text-align: center;
    font-family: "Montserrat", sans-serif;
    font-weight: 700;
    font-size: 34px;
    color: var(--volume-yellow);
  }
</style>
</head>
<body>
  <main class="canvas">
    <section class="label">
      <div class="label__emblem-area" role="img" aria-label="Decorative concentric green and lime arcs behind the brand name"></div>
      <h1 class="label__brand">Doctor<br>Quaffel</h1>
      <p class="label__slogan">Powerd by Nature</p>
      <div class="label__band">
        <p class="label__product">All Purpus cleaner</p>
      </div>
      <p class="label__volume">750ml</p>
    </section>
  </main>
</body>
</html>
```